Awesome photographers card for an awesome new business

Double sided business card Black background and silver logo in middle on one side. Details on otherside. please keep it simple

Photographer

Gavin Tolley
0482615073
GavinTolleyPhotography82@lumenpost.com
www.GavinTolleyPhotography.com.au
Instagram _Gavin_tolley

Requirements
Must have
• My logo in Silver
• please use instagram logo instead of "Instagram"

```html
<!DOCTYPE html>
<html lang="en">
<head>
<meta charset="utf-8">
<title>Gavin Tolley Photography – Business Card</title>
<link rel="stylesheet" href="https://fonts.googleapis.com/css2?family=Kaushan+Script&family=Montserrat:wght@500&family=Open+Sans:wght@400&display=swap">
<style>
  :root {
    --page: #ffffff;
    --card-deep: #060606;
    --card-panel: #141414;
    --card-back: #121212;
    --silver: #c4c4c4;
    --silver-faint: rgba(200, 200, 200, 0.08);
    --text-light: #e6e6e6;
    --icon: #d8d8d8;
  }
  * { box-sizing: border-box; margin: 0; padding: 0; }
  html, body {
    width: 1200px;
    height: 1200px;
    overflow: hidden;
    background: var(--page);
  }
  .sheet { position: relative; width: 1200px; height: 1200px; }

  .card {
    position: absolute;
    left: 154px;
    width: 900px;
    height: 540px;
    overflow: hidden;
  }
  .card--front { top: 42px; background: var(--card-panel); }
  .card--back { top: 616px; background: var(--card-back); }

  .card__brand-panel {
    position: absolute;
    left: 0; top: 0;
    width: 403px; height: 100%;
    background: var(--card-deep);
  }

  /* brand seal: plain circle with the business name set in type */
  .seal {
    position: absolute;
    border-radius: 50%;
    border: 3px solid var(--silver);
    display: flex;
    flex-direction: column;
    align-items: center;
    justify-content: center;
    font-family: "Montserrat", sans-serif;
    font-weight: 500;
    color: var(--silver);
    text-align: center;
  }
  .seal--small {
    left: 66px; top: 122px;
    width: 288px; height: 288px;
    font-size: 25px;
    letter-spacing: 6px;
    gap: 12px;
  }
  .seal--small .seal__sub { font-size: 11px; letter-spacing: 5px; }
  .seal--large {
    left: 274px; top: 76px;
    width: 376px; height: 376px;
    font-size: 33px;
    letter-spacing: 8px;
    gap: 16px;
  }
  .seal--large .seal__sub { font-size: 14px; letter-spacing: 7px; }
  .seal--ghost {
    left: 560px; top: 200px;
    width: 400px; height: 400px;
    border-color: var(--silver-faint);
    color: var(--silver-faint);
    font-size: 34px;
    letter-spacing: 8px;
    gap: 16px;
  }
  .seal--ghost .seal__sub { font-size: 14px; letter-spacing: 7px; }

  .identity {
    position: absolute;
    left: 458px; top: 140px;
  }
  .identity__name {
    font-family: "Kaushan Script", cursive;
    font-size: 50px;
    line-height: 1;
    color: var(--text-light);
  }
  .identity__role {
    font-family: "Open Sans", sans-serif;
    font-size: 17px;
    color: var(--text-light);
    margin: 4px 0 0 96px;
  }

  .contacts {
    position: absolute;
    left: 458px; top: 346px;
    list-style: none;
    font-family: "Open Sans", sans-serif;
    font-size: 17.5px;
    color: var(--text-light);
  }
  .contacts__item {
    display: flex;
    align-items: center;
    height: 33.5px;
  }
  .contacts__icon {
    width: 22px; height: 22px;
    margin-right: 18px;
    flex: none;
  }
</style>
</head>
<body>
<main class="sheet">

  <section class="card card--front" aria-label="Business card, details side">
    <div class="card__brand-panel">
      <div class="seal seal--small">
        <span class="seal__name">GAVIN TOLLEY</span>
        <span class="seal__sub">PHOTOGRAPHY</span>
      </div>
    </div>

    <div class="seal seal--ghost" aria-hidden="true">
      <span class="seal__name">GAVIN TOLLEY</span>
      <span class="seal__sub">PHOTOGRAPHY</span>
    </div>

    <div class="identity">
      <p class="identity__name">Gavin Tolley</p>
      <p class="identity__role">Photographer</p>
    </div>

    <ul class="contacts">
      <li class="contacts__item">
        <svg class="contacts__icon" viewBox="0 0 24 24" aria-hidden="true">
          <path fill="var(--icon)" d="M6.6 10.8a15.1 15.1 0 0 0 6.6 6.6l2.2-2.2c.3-.3.7-.4 1-.2 1.1.4 2.3.6 3.6.6.6 0 1 .4 1 1V20c0 .6-.4 1-1 1A17 17 0 0 1 3 4c0-.6.4-1 1-1h3.5c.6 0 1 .4 1 1 0 1.3.2 2.5.6 3.6.1.3 0 .7-.2 1z"/>
        </svg>
        <span>0482615073</span>
      </li>
      <li class="contacts__item">
        <svg class="contacts__icon" viewBox="0 0 24 24" aria-hidden="true">
          <rect x="2" y="5" width="20" height="14" fill="none" stroke="var(--icon)" stroke-width="1.8"/>
          <path d="M2 5l10 8 10-8" fill="none" stroke="var(--icon)" stroke-width="1.8"/>
        </svg>
        <span>GavinTolleyPhotography82@lumenpost.com</span>
      </li>
      <li class="contacts__item">
        <svg class="contacts__icon" viewBox="0 0 24 24" aria-hidden="true">
          <circle cx="12" cy="12" r="10.5" fill="none" stroke="var(--icon)" stroke-width="1.6"/>
          <text x="12" y="14.5" text-anchor="middle" font-family="Open Sans, sans-serif" font-size="7" font-weight="700" fill="var(--icon)">www</text>
        </svg>
        <span>www.GavinTolleyPhotography.com.au</span>
      </li>
      <li class="contacts__item">
        <svg class="contacts__icon" viewBox="0 0 24 24" aria-hidden="true">
          <rect x="3" y="3" width="18" height="18" rx="2" fill="var(--icon)"/>
        </svg>
        <span>_Gavin_tolley</span>
      </li>
    </ul>
  </section>

  <section class="card card--back" aria-label="Business card, brand side">
    <div class="seal seal--large">
      <span class="seal__name">GAVIN TOLLEY</span>
      <span class="seal__sub">PHOTOGRAPHY</span>
    </div>
  </section>

</main>
</body>
</html>
```